VelaCure Wellness Business Cards

I am looking to have luxury business cards made for my IV Therapy and Wellness business.
Updates

Target Market(s)

Health and Wellness professionals

Industry/Entity Type

MedSpa

Contact Information for Business Card

Tobin Haverly, MSN, RN, CCRN Tobin@velacurewellness.com (916) 582-3179 QR code to website www.velacurewellness.com

```html
<!DOCTYPE html>
<html lang="en">
<head>
<meta charset="utf-8">
<title>VelaCure Wellness Business Cards</title>
<link href="https://fonts.googleapis.com/css2?family=Poppins:wght@400;500;600&display=swap" rel="stylesheet">
<style>
  :root {
    --stage: #2a2a2e;
    --navy: #2b2466;
    --gold: #ad8b3a;
    --sky: #22a6e0;
    --white: #ffffff;
  }
  * { margin: 0; padding: 0; box-sizing: border-box; }
  html, body {
    width: 1200px; height: 801px; overflow: hidden;
    background: var(--stage);
    font-family: "Poppins", sans-serif;
  }
  .stage {
    position: relative; width: 1200px; height: 801px;
    display: flex; align-items: center; justify-content: center; gap: 54px;
  }
  .card {
    position: relative; width: 520px; height: 297px; overflow: hidden;
    box-shadow: 0 18px 40px rgba(0,0,0,.45);
  }
  .wordmark {
    display: flex; align-items: center; gap: 8px;
    font-weight: 600; white-space: nowrap; line-height: 1;
  }
  .wordmark__dot { border-radius: 50%; flex: none; }

  /* Back */
  .card--back {
    background: var(--navy);
    display: flex; align-items: center; justify-content: space-around; padding: 0 26px;
  }
  .card--back .wordmark--primary { color: var(--white); font-size: 24px; }
  .wordmark--primary .wordmark__dot { width: 13px; height: 13px; background: var(--sky); }
  .wordmark--gold { color: var(--gold); font-size: 15px; font-weight: 500; }
  .wordmark--gold .wordmark__dot { width: 9px; height: 9px; background: var(--gold); }

  /* Front */
  .card--front { background: var(--white); }
  .front__brand {
    position: absolute; left: 0; right: 0; top: 0; height: 170px;
    display: flex; align-items: center; justify-content: space-between; padding: 0 30px;
  }
  .front__brand .wordmark--primary { color: var(--navy); font-size: 24px; }
  .front__nameband {
    position: absolute; left: 0; right: 0; top: 170px; height: 34px;
    background: var(--gold); color: var(--white);
    display: flex; align-items: center; padding-left: 30px; gap: 9px; white-space: nowrap;
  }
  .person__name { font-weight: 600; font-size: 14px; letter-spacing: .4px; text-transform: uppercase; }
  .person__credentials { font-weight: 500; font-size: 11px; letter-spacing: .4px; }
  .person__sep { font-size: 15px; font-weight: 400; }
  .person__title { font-size: 10.5px; letter-spacing: .8px; text-transform: uppercase; }
  .front__contactband {
    position: absolute; left: 0; right: 0; top: 204px; height: 72px;
    background: var(--navy); color: var(--white);
    display: grid; grid-template-columns: 170px 1px 1fr; align-items: center; padding: 0 30px;
    font-size: 12px;
  }
  .contact__divider { width: 1px; height: 30px; background: var(--sky); }
  .contact__group { display: flex; flex-direction: column; gap: 6px; white-space: nowrap; }
  .contact__group--right { padding-left: 40px; }
  .contact__row { display: flex; align-items: center; gap: 8px; }
  .contact__icon { width: 12px; height: 12px; flex: none; }
  .contact__accent { color: var(--sky); }
  .front__rule { position: absolute; left: 0; right: 0; top: 276px; height: 4px; background: var(--white); }
  .front__strip { position: absolute; left: 0; right: 0; top: 280px; bottom: 0; background: var(--sky); }
</style>
</head>
<body>
<main class="stage">
  <section class="card card--back" aria-label="Card back">
    <div class="wordmark wordmark--primary"><span class="wordmark__dot"></span>VelaCure Wellness</div>
    <div class="wordmark wordmark--gold"><span class="wordmark__dot"></span>VelaCure Wellness</div>
  </section>

  <section class="card card--front" aria-label="Card front">
    <div class="front__brand">
      <div class="wordmark wordmark--primary"><span class="wordmark__dot"></span>VelaCure Wellness</div>
      <div class="wordmark wordmark--gold"><span class="wordmark__dot"></span>VelaCure Wellness</div>
    </div>
    <div class="front__nameband">
      <span class="person__name">Tobin Haverly</span>
      <span class="person__credentials">MSN, RN, CCRN</span>
      <span class="person__sep">|</span>
      <span class="person__title">Managing Partner</span>
    </div>
    <div class="front__contactband">
      <div class="contact__group">
        <div class="contact__row">
          <svg class="contact__icon" viewBox="0 0 12 12"><path fill="#22a6e0" d="M2.5 1l2 2.2-1 1.3a7 7 0 0 0 4 4l1.3-1 2.2 2-1.3 1.8C5.5 11 1 6.5.7 2.3z"/></svg>
          <span>(916) 582-3179</span>
        </div>
        <div class="contact__row">
          <svg class="contact__icon" viewBox="0 0 12 12"><rect x="3" y=".8" width="6" height="10.4" rx="1" fill="none" stroke="#22a6e0" stroke-width="1.2"/></svg>
          <span>(916) 582-3179</span>
        </div>
      </div>
      <span class="contact__divider"></span>
      <div class="contact__group contact__group--right">
        <div class="contact__row">
          <svg class="contact__icon" viewBox="0 0 12 12"><rect x=".5" y="2" width="11" height="8" fill="#22a6e0"/><path d="M.5 2l5.5 4.5L11.5 2" fill="none" stroke="#fff" stroke-width="1"/></svg>
          <span>Tobin@velacurewellness.com</span>
        </div>
        <div class="contact__row">
          <svg class="contact__icon" viewBox="0 0 12 12"><g fill="none" stroke="#22a6e0" stroke-width="1"><circle cx="6" cy="6" r="5"/><ellipse cx="6" cy="6" rx="2.2" ry="5"/><path d="M1 6h10"/></g></svg>
          <span>www.<span class="contact__accent">velacurewellness</span>.com</span>
        </div>
      </div>
    </div>
    <div class="front__rule"></div>
    <div class="front__strip"></div>
  </section>
</main>
</body>
</html>
```